" Pessoal, vamos lá! Estivemos trabalhando bastante e definindo o formato da nossa empresa e agora chegou a hora de passarmos para o nosso web site. Vamos lá: O " ÍNDICE" deverá conter: Nossos Serviços, SUA REFORMA PROTEGIDA, Tudo Melhor para Você, Peça um orçamento. 1- Ao clicar na aba Nossos Serviços. Será direcionado para Reforma & Construção; e Assessoria. Nesse campo terá as seguintes informações: Reforma & Construção * Projeto Guia de Reforma Fornecemos a planta com alterações e novas medidas. * Orçamento Enviamos nossa proposta de orçamento totalmente grátis. * Acompanhamento de Engenheiro Civil e Arquiteto* Equipe de profissionais capacitados. * Cotação de melhores preços de materiais; Auxiliamos na busca de melhores preços e condições de pagamento para a sua lar renovo ou obra. * Seleção de parceiros para execução; Selecionamos profissionais capacitados para a execução da sua lar renovo ou obra. Assessoria * Acompanhamos o projeto em execução Acompanhamento das atividades associadas ao planejamento, organização, direção e controle necessários para garantir o sucesso da sua lar renovo ou obra. * Programação da Obra Compreendendo o detalhamento dos serviços e as providências preliminares, a programação dos materiais, mão de obra e equipamentos. * Relatórios de Andamento da obra Adequação do projeto e da construção às necessidades do cliente no que se refere à qualidade, prazo e custo. 2- Na aba " SUA REFORMA PROTEGIDA" ao clicar será direcionado para o campo com as seguintes informações: * Substituição de materiais danificados Qualquer material danificado por nossos profissionais ou fornecedores são repostos na mesma qualidade e quantidade, sem custos para o cliente. * Correção dos serviços mal executados* Mesmo buscando fornecer o resultado que você espera e sempre trabalhando com profissionais capacitados, erros podem acontecer. Diante disso, asseguramos a conclusão da sua obra com qualidade. * Troca de fornecedor Selecionamos os melhores profissionais do mercado. Mesmo assim, se você não gostar, é livre para nos solicitar a troca. 3- Já na aba " Tudo melhor para você" teremos as seguintes informações: * Orçamento gratuito * Gestão de pagamento * Prazo e rapidez * Saiba tudo que está acontecendo na sua lar renovo * Garantia de Satisfação * Consultoria Técnica * Cronograma de gerenciamento * Otimização de custos * Equipe preparada 4- Seja um Novo Parceiro Ao clicar nessa frase aparecerá em uma nova janela duas opçoes: EMPRESA e PROFISSIONAL. Clicando em EMPRESA ficará a disposição para preenchimento os seguintes campos: Nome da Empresa, Nome do Responsável, Cidade, email, contato, área de especialidade ( nesse campo existirá opções para preenchimento) e campo para apresentação da empresa. Se clicar em PROFISSIONAL terá a disposição os seguintes itens: Nome, Telefone, cidade, email e área de especialidade (também várias opções )e um campo para digitação chamado de ESCREVA AQUI SUA MENSAGEM. 5- ORÇAMENTO Após o clique no ORÇAMENTO, o cliente terá à disposição 3 opções para um novo clique: REFORMA, CONSTRUÇÃO, ASSESSORIA (se possível, adicionar imagens aos nomes) • Após o clique em REFORMA abrirá um formulário com opções: Campo com opções de escolha de Casa, Apartamento ou loja comercial; Escolha do Cômodo (terá opções nesse campo) e nova janela referente a esta escolha para a digitação do tipo de serviço a ser executado nesse campo. Caso existam mais cômodos, existirá a opção de adicionar; opção de upload de arquivo; e campo para escrever alguma mensagem ou observação. • Clicando em CONSTRUÇÃO – O que pretende construir?; descreva detalhadamente o que pretende construir; opção de upload de arquivo; e campo para escrever alguma mensagem ou observação. • ASSESSORIA – Ajudamos você na gestão da sua lar renovo. Como podemos ajudar? (aparecerá as opções de Cotação de preços; Busca de profissionais; Conferência e acompanhamento de serviços executados); descreva detalhadamente que tipo de ajuda você precisa em sua obra. 5.1 Ao final de todas as opções aparecerá campo para preenchimento dos dados do cliente: Seu nome; email; CEP; Rua; Numero/complemento; Bairro; Cidade; Estado; Telefone; e campo para clique em Aceito e concordo com os Termos de Uso e a Política de Privacidade. Confirmar envio da solicitação Para auxiliá-los vejam o site http://www.lajetorvix.com.br/orcamento.html 6- Vale lembrar que em cada aba terá que ser visualizado a opção de PEÇA UM ORÇAMENTO, FAÇA SUA LAR RENOVO, SUA LAR RENOVO AGORA.... FIQUEM A VONTADE com os dizeres. - Ao Final, na parte de contatos, endereço, rede social.... etc. Gostaríamos de deixar o espaço SEJA UM PARCEIRO. Queremos que ao clicar nessa item a empresa preencha um questionário. 7- Vale lembrar que ao clicar no item Peça orçamento o cliente será direcionado para um campo de preenchimento de dados. OBS IMPORTANTE: - Façam o uso de imagens modernas e suaves.. Queremos ser diferentes e inovadores e precisamos muito da criatividade de vocês. - Segue anexo um modelo de imagem que gostamos Segue anexo do escopo do nosso portfólio que será a cópia do nosso site. Aproveitem. "

```html
<!DOCTYPE html>
<html lang="pt-BR">
<head>
<meta charset="utf-8">
<title>lar renovo — Reforma, Construção e Assessoria</title>
<link rel="stylesheet" href="https://fonts.googleapis.com/css2?family=Open+Sans:wght@300;400;600;700&display=swap">
<style>
  :root {
    --navy-deep: #172c4a;
    --navy: #1f3b63;
    --navy-light: #2b5283;
    --blue: #3a86c8;
    --blue-soft: #5ea3de;
    --ink: #2a3d57;
    --muted: #7d8ba0;
    --white: #ffffff;
    --paper: #f3f5f8;
    --circle: #e6ebf1;
  }
  * { box-sizing: border-box; margin: 0; padding: 0; }
  html, body { width: 1200px; height: 1200px; overflow: hidden; }
  body { font-family: "Open Sans", Arial, sans-serif; background: var(--paper); color: var(--ink); }
  .page { width: 1200px; height: 1200px; display: flex; flex-direction: column; }

  .site-header {
    height: 90px; background: var(--navy-deep);
    display: flex; align-items: center; justify-content: space-between;
    padding: 0 56px;
  }
  .brand { display: flex; align-items: center; gap: 12px; }
  .brand-square { width: 30px; height: 30px; background: var(--white); }
  .brand-name { color: var(--white); font-weight: 400; font-size: 24px; letter-spacing: .5px; }
  .main-nav { display: flex; align-items: center; gap: 28px; }
  .nav-link { color: var(--white); font-size: 12px; font-weight: 600; letter-spacing: .8px; text-decoration: none; }
  .nav-link.is-active { border: 1px solid rgba(255,255,255,.6); padding: 7px 12px; }
  .social-dot { width: 22px; height: 22px; border-radius: 50%; background: rgba(255,255,255,.25); }
  .quote-button {
    background: var(--blue); color: var(--white); font-size: 12px; font-weight: 700;
    letter-spacing: 1px; padding: 10px 20px; text-decoration: none;
  }

  .services-hero {
    height: 480px;
    background: linear-gradient(120deg, var(--navy) 0%, var(--navy-light) 55%, var(--navy) 100%);
    color: var(--white); text-align: center; padding-top: 60px;
  }
  .section-title { font-size: 40px; font-weight: 600; letter-spacing: 5px; }
  .hero-items { display: flex; justify-content: center; gap: 90px; margin-top: 56px; }
  .hero-item { width: 240px; }
  .item-title { font-size: 14px; font-weight: 700; letter-spacing: 1.2px; text-transform: uppercase; line-height: 1.4; }
  .item-text { font-size: 13px; line-height: 1.55; margin-top: 10px; opacity: .85; }
  .hero-icon { width: 70px; height: 70px; margin: 26px auto 0; background: rgba(255,255,255,.9); border-radius: 6px; }
  .slider-dots { display: flex; justify-content: center; gap: 10px; margin-top: 46px; }
  .slider-dots span { width: 40px; height: 3px; background: rgba(255,255,255,.35); }
  .slider-dots span.is-current { background: var(--white); }

  .advisory {
    height: 390px; background: var(--white); text-align: center; padding-top: 50px;
  }
  .advisory .section-title { color: var(--navy); font-size: 36px; }
  .title-rule { width: 70px; height: 3px; background: var(--blue); margin: 14px auto 0; }
  .advisory-items { display: flex; justify-content: center; gap: 90px; margin-top: 40px; }
  .advisory-item { width: 240px; }
  .advisory-item .item-title { color: var(--navy); }
  .advisory-item .item-text { color: var(--muted); opacity: 1; }
  .advisory-icon { width: 84px; height: 84px; border-radius: 50%; margin: 22px auto 0; background: var(--circle); }

  .brand-band {
    flex: 1; background: linear-gradient(135deg, var(--blue) 0%, var(--blue-soft) 100%);
    display: flex; align-items: center; justify-content: center; gap: 30px; color: var(--white);
  }
  .band-square { width: 110px; height: 110px; background: var(--white); }
  .band-name { font-size: 76px; font-weight: 400; line-height: 1; letter-spacing: 1px; }
  .band-tagline { font-size: 20px; font-weight: 600; letter-spacing: 2px; margin-top: 12px; }
</style>
</head>
<body>
<div class="page">
  <header class="site-header">
    <div class="brand">
      <div class="brand-square"></div>
      <span class="brand-name">lar renovo</span>
    </div>
    <nav class="main-nav">
      <a class="nav-link is-active" href="#servicos">NOSSOS SERVIÇOS</a>
      <a class="nav-link" href="#protegida">SUA REFORMA PROTEGIDA</a>
      <a class="nav-link" href="#melhor">TUDO MELHOR PARA VOCÊ</a>
      <span class="social-dot" aria-label="Rede social"></span>
      <a class="quote-button" href="#orcamento">ORÇAMENTO</a>
    </nav>
  </header>

  <section class="services-hero" id="servicos">
    <h1 class="section-title">Reforma &amp; Construção</h1>
    <div class="hero-items">
      <div class="hero-item">
        <h2 class="item-title">Projeto guia<br>de reforma</h2>
        <p class="item-text">Fornecemos a planta com alterações e novas medidas.</p>
        <div class="hero-icon" role="img" aria-label="Ícone de planta de casa"></div>
      </div>
      <div class="hero-item">
        <h2 class="item-title">Orçamento<br>sem compromisso</h2>
        <p class="item-text">Enviamos nossa proposta de orçamento totalmente grátis.</p>
        <div class="hero-icon" role="img" aria-label="Ícone de documento de orçamento"></div>
      </div>
      <div class="hero-item">
        <h2 class="item-title">Acompanhamento<br>de profissionais</h2>
        <p class="item-text">Equipe de profissionais capacitados e engenheiros.</p>
        <div class="hero-icon" role="img" aria-label="Ícone de profissional de obra"></div>
      </div>
    </div>
    <div class="slider-dots"><span class="is-current"></span><span></span></div>
  </section>

  <section class="advisory">
    <h1 class="section-title">Assessoria</h1>
    <div class="title-rule"></div>
    <div class="advisory-items">
      <div class="advisory-item">
        <h2 class="item-title">Acompanhamos<br>o projeto em execução</h2>
        <p class="item-text">Acompanhamento das atividades até a conclusão da obra.</p>
        <div class="advisory-icon" role="img" aria-label="Ícone de ferramentas"></div>
      </div>
      <div class="advisory-item">
        <h2 class="item-title">Programação<br>de obra</h2>
        <p class="item-text">Detalhamento dos serviços, materiais e equipamentos.</p>
        <div class="advisory-icon" role="img" aria-label="Ícone de cronograma"></div>
      </div>
      <div class="advisory-item">
        <h2 class="item-title">Relatórios de<br>andamento da obra</h2>
        <p class="item-text">Adequação à qualidade, prazo e custo do cliente.</p>
        <div class="advisory-icon" role="img" aria-label="Ícone de relatório"></div>
      </div>
    </div>
  </section>

  <footer class="brand-band">
    <div class="band-square"></div>
    <div>
      <div class="band-name">lar renovo</div>
      <div class="band-tagline">REFORMA, CONSTRUÇÃO E ASSESSORIA</div>
    </div>
  </footer>
</div>
</body>
</html>
```